Packaging design for guitar parts and accesories

We need a packaging design for our large range of small/medium sized guitar parts. The design will be used on sealable poly bags of varying sizes ( 3" to around 7"). We have a logo that we'd like incorporated into the design.

The bags will be transparent on the front, and opaque on the back.
We'd like the back to contain some company info - web address, telephone number etc..

Please visit our website for an idea of what we do - www.harbourlanestrings.co.uk

Design must have a blank space on the front so that the product is at least partially visible.

Ideally we're looking for quite a minimalist design. Less is more as they say.

Approximate bag sizes will be:

3 x 3.25"
4 x 5.5"
5 x 7.5"
10 x 14"

Please let me know if you need any further info.

Target Market(s)

males, aged 25-65

Colors
ec1f27
000000

Requirements
Must have
• Space for barcode on rear of packaging
• Company address, phone number, web address on rear of packaging

```html
<!DOCTYPE html>
<html lang="en">
<head>
<meta charset="utf-8">
<title>Bronze Acoustic Guitar Strings – Harbour Lane Strings</title>
<link rel="stylesheet" href="https://fonts.googleapis.com/css2?family=Lobster&display=swap">
<style>
  :root {
    --ink: #000000;
    --brand-red: #ec1f27;
    --cream: #f6d6b2;
    --cocoa: #4a2414;
    --amber: #d9822b;
    --amber-deep: #a8561a;
    --photo-warm: #5a3a22;
    --photo-mid: #2a1a10;
  }
  * { margin: 0; padding: 0; box-sizing: border-box; }
  html, body { width: 944px; height: 1200px; overflow: hidden; background: var(--ink); }
  .pack {
    position: relative;
    width: 944px;
    height: 1200px;
    background: var(--ink);
    font-family: "Lobster", cursive;
    overflow: hidden;
  }
  .pack__photo {
    position: absolute;
    inset: 0 0 260px 0;
    background:
      radial-gradient(ellipse at 18% 40%, rgba(190,140,70,.55), transparent 45%),
      radial-gradient(ellipse at 70% 50%, rgba(120,80,50,.5), transparent 50%),
      linear-gradient(180deg, var(--photo-warm) 0%, var(--photo-mid) 55%, var(--ink) 100%);
  }
  .headline {
    position: absolute;
    left: 0; right: 0;
    text-align: center;
    color: var(--cocoa);
    line-height: 1;
    text-shadow:
      -3px -3px 0 var(--cream), 3px -3px 0 var(--cream),
      -3px 3px 0 var(--cream), 3px 3px 0 var(--cream),
      0 -3px 0 var(--cream), 0 3px 0 var(--cream),
      -3px 0 0 var(--cream), 3px 0 0 var(--cream),
      5px 6px 6px rgba(0,0,0,.6);
  }
  .headline--material { top: 52px; font-size: 50px; }
  .headline--product { top: 145px; font-size: 60px; }
  .headline--strings { top: 235px; font-size: 124px; }
  .gauge-badge {
    position: absolute;
    left: 371px;
    top: 675px;
    width: 180px;
    height: 150px;
  }
  .brand {
    position: absolute;
    left: 0; right: 0;
    top: 1010px;
    text-align: center;
    font-size: 84px;
    color: var(--brand-red);
    line-height: 1;
  }
</style>
</head>
<body>
<main class="pack">
  <div class="pack__photo" role="img" aria-label="Close-up photo of a hand fretting a chord on an acoustic guitar neck, warm dim light"></div>

  <h1>
    <span class="headline headline--material">Bronze</span>
    <span class="headline headline--product">Acoustic Guitar</span>
    <span class="headline headline--strings">Strings</span>
  </h1>

  <svg class="gauge-badge" viewBox="0 0 180 150" aria-label="Light gauge .012-.052">
    <circle cx="90" cy="68" r="66" fill="var(--cream)"/>
    <circle cx="90" cy="68" r="58" fill="var(--amber)"/>
    <text x="90" y="70" text-anchor="middle" font-family="Lobster, cursive" font-size="44" fill="var(--cocoa)" stroke="var(--cream)" stroke-width="1.5">light</text>
    <path d="M6 92 L174 92 L164 108 L174 124 L6 124 L16 108 Z" fill="var(--amber-deep)" stroke="var(--cream)" stroke-width="3"/>
    <text x="90" y="117" text-anchor="middle" font-family="Lobster, cursive" font-size="26" fill="var(--cream)">.012-.052</text>
  </svg>

  <p class="brand">Harbour Lane Strings</p>
</main>
</body>
</html>
```